Company rebrand announcement

We're renaming and rebranding. our company - I need an email design that we can send out as an update to our customers and suppliers. I can provide the text but would like the design to allow me to write the text myself as we would like to personalise it and mail merge. But will be something like this:

The past year has been incredible for k7webworks and Quiet Harbor. If you've been following our story you'll know we've been working hard at being a couple over the last year and now we're ready to make it official!

As part of the official merge we'll be renaming to wefoundtrail - a name that highlights our passion for connecting people and technology helping make our everyday lives that little bit easier.

With a new name comes a few changes, new website, new logo, new clothes - the excitement is real! THE MOST exciting parts though are that we have the same great team and will continue to provide the same great service with the agility and trust you have come to love and expect from us.

We'll send out the details over the coming weeks to make sure we all stay connected and if you have any questions in the meantime or anything you need us to do, please reach out to any one of us and we'll get right back to you.

Thanks,
Edith, Greg and Wade

```html
<!DOCTYPE html>
<html lang="en">
<head>
<meta charset="utf-8">
<title>wefoundtrail – rebrand announcement</title>
<link href="https://fonts.googleapis.com/css2?family=Sora:wght@400;600;700&family=Arimo:wght@400&display=swap" rel="stylesheet">
<style>
:root{
  --yellow:#fcc419;
  --yellow-deep:#e9b40f;
  --ink:#111111;
  --dark:#1c1c1c;
  --white:#ffffff;
  --hero-a:#1d2530;
  --hero-b:#4a3b22;
}
*{margin:0;padding:0;box-sizing:border-box}
html,body{width:1200px;height:2721px;overflow:hidden;background:var(--white)}
body{position:relative;font-family:"Arimo",Arial,sans-serif;color:var(--ink)}

.topbar{position:absolute;left:0;top:0;width:1200px;height:101px;background:var(--white);z-index:2}
.call{position:absolute;left:74px;top:28px;display:flex;align-items:center;gap:14px}
.call-icon{width:44px;height:44px;border-radius:50%;background:var(--yellow);border:2px solid var(--ink);display:flex;align-items:center;justify-content:center}
.call-label{font-family:"Sora",sans-serif;font-size:13px;font-weight:600;line-height:1}
.call-number{font-family:"Sora",sans-serif;font-size:23px;font-weight:600;line-height:1.2}
.brand-disc{position:absolute;left:497px;top:-20px;width:206px;height:206px;border-radius:50%;background:var(--white);z-index:3;display:flex;flex-direction:column;align-items:center;justify-content:flex-end;padding-bottom:52px;gap:8px}
.brand-dot{width:22px;height:22px;background:var(--yellow)}
.brand-name{font-family:"Sora",sans-serif;font-size:26px;font-weight:600;color:var(--ink)}
.social{position:absolute;left:1013px;top:31px;width:38px;height:38px;border-radius:50%;border:2px solid var(--ink)}

.hero{position:absolute;left:0;top:101px;width:1200px;height:626px;background:radial-gradient(ellipse at 55% 55%,#5a4a2a 0%,var(--hero-b) 25%,var(--hero-a) 75%)}
.hero-title{position:absolute;left:0;top:222px;width:1200px;text-align:center;font-family:"Sora",sans-serif;font-weight:600;font-size:90px;line-height:1.1;color:var(--white);letter-spacing:-2px}
.hero-tag{position:absolute;left:0;top:349px;width:1200px;text-align:center;font-family:"Sora",sans-serif;font-weight:700;font-size:28px;color:var(--yellow)}

.intro-card{position:absolute;left:82px;top:819px;width:1037px;height:329px;border-radius:20px;background:linear-gradient(135deg,var(--yellow),var(--yellow-deep));text-align:center;padding:60px 58px 0}
.intro-card h2{font-family:"Sora",sans-serif;font-weight:600;font-size:44px;line-height:1.2;margin-bottom:18px}
.intro-card p{font-size:20px;line-height:36px}

.merge{position:absolute;left:0;top:1245px;width:1200px;height:759px;background:var(--white)}
.merge-wedge{position:absolute;left:0;top:0}
.merge-photo{position:absolute;left:48px;top:85px;width:429px;height:552px;border-radius:34px;background:linear-gradient(160deg,#4a4a4a,#8c8c8c 55%,#3a3a3a)}
.merge-copy{position:absolute;left:533px;top:86px;width:600px}
.merge-copy h2{font-family:"Sora",sans-serif;font-weight:600;font-size:41px;line-height:53px;margin-bottom:26px}
.merge-copy p{font-size:20.5px;line-height:43px}
.merge-copy p + p{margin-top:43px}

.signoff{position:absolute;left:0;top:2004px;width:1200px;height:384px;background:var(--dark);text-align:center;padding-top:56px;color:var(--white)}
.signoff p{font-family:"Sora",sans-serif;font-weight:600;font-size:24px;line-height:41px;width:850px;margin:0 auto}
.signoff .thanks{font-family:"Sora",sans-serif;font-weight:600;font-size:41px;color:var(--yellow);margin-top:18px}
.signoff .names{font-family:"Sora",sans-serif;font-weight:600;font-size:19px;margin-top:6px}

.footer{position:absolute;left:0;top:2388px;width:1200px;height:333px}
.footer-brand{position:absolute;left:80px;top:110px;display:flex;align-items:center;gap:12px}
.footer-brand .brand-dot{width:28px;height:28px}
.footer-brand .brand-name{font-size:34px}
.contact{position:absolute;top:140px;display:flex;align-items:center;gap:14px}
.contact-icon{width:44px;height:44px;border-radius:50%;background:var(--yellow);display:flex;align-items:center;justify-content:center}
.contact b{display:block;font-family:"Sora",sans-serif;font-size:15px;font-weight:600}
.contact span{font-family:"Sora",sans-serif;font-size:14px}
.copyright{position:absolute;left:372px;top:243px;font-family:"Sora",sans-serif;font-size:19px}
</style>
</head>
<body>

<header class="topbar">
  <div class="call">
    <div class="call-icon">
      <svg width="20" height="20" viewBox="0 0 24 24"><path d="M6.6 10.8a15 15 0 0 0 6.6 6.6l2.2-2.2c.3-.3.7-.4 1-.2 1.1.4 2.3.6 3.6.6.6 0 1 .4 1 1V20c0 .6-.4 1-1 1A17 17 0 0 1 3 4c0-.6.4-1 1-1h3.5c.6 0 1 .4 1 1 0 1.3.2 2.5.6 3.6.1.3 0 .7-.2 1z" fill="#111"/></svg>
    </div>
    <div>
      <div class="call-label">call us</div>
      <div class="call-number">+44 3300 555 019</div>
    </div>
  </div>
  <div class="social" aria-label="social profile"></div>
</header>

<div class="brand-disc">
  <div class="brand-dot"></div>
  <div class="brand-name">wefoundtrail</div>
</div>

<section class="hero" role="img" aria-label="Photo of several hands holding smartphones, dark warm tones">
  <h1 class="hero-title">wefoundtrail</h1>
  <div class="hero-tag">CONNECTING PEOPLE, EVERY DAY</div>
</section>

<section class="intro-card">
  <h2>past year</h2>
  <p>The past year has been incredible for k7webworks and Quiet Harbor. If you've been following our story you'll know we've been working hard at being a couple over the last year and now we're ready to make it official!</p>
</section>

<section class="merge">
  <svg class="merge-wedge" width="500" height="759" viewBox="0 0 500 759"><polygon points="0,0 499,0 0,780" fill="#fcc419"/></svg>
  <div class="merge-photo" role="img" aria-label="Photo of a smiling woman looking at her smartphone"></div>
  <div class="merge-copy">
    <h2>as part of the official merge we'll be renaming to wefoundtrail</h2>
    <p>&nbsp;a name that highlights our passion for connecting people and technology helping make our everyday lives that little bit easier.</p>
    <p>With a new name comes a few changes, new website, new logo, new clothes - the excitement is real! THE MOST exciting parts though are that we have the same great team and will continue to provide the same great service with the agility and trust you have come to love and expect from us.</p>
  </div>
</section>

<section class="signoff">
  <p>We'll send out the details over the coming weeks to make sure we all stay connected and if you have any questions in the meantime or anything you need us to do, please reach out to any one of us and we'll get right back to you.</p>
  <div class="thanks">thanks</div>
  <div class="names">edith, greg and wade</div>
</section>

<footer class="footer">
  <div class="footer-brand">
    <div class="brand-dot"></div>
    <div class="brand-name">wefoundtrail</div>
  </div>
  <div class="contact" style="left:366px">
    <div class="contact-icon"><svg width="18" height="22" viewBox="0 0 24 30"><path d="M12 0a10 10 0 0 0-10 10c0 7.5 10 20 10 20s10-12.5 10-20A10 10 0 0 0 12 0zm0 14a4 4 0 1 1 0-8 4 4 0 0 1 0 8z" fill="#111"/></svg></div>
    <div><b>location</b><span>Northgate and Eastbrook offices</span></div>
  </div>
  <div class="contact" style="left:686px">
    <div class="contact-icon"><svg width="20" height="20" viewBox="0 0 24 24"><path d="M6.6 10.8a15 15 0 0 0 6.6 6.6l2.2-2.2c.3-.3.7-.4 1-.2 1.1.4 2.3.6 3.6.6.6 0 1 .4 1 1V20c0 .6-.4 1-1 1A17 17 0 0 1 3 4c0-.6.4-1 1-1h3.5c.6 0 1 .4 1 1 0 1.3.2 2.5.6 3.6.1.3 0 .7-.2 1z" fill="#111"/></svg></div>
    <div><b>phone</b><span>+44 3300 555 019</span></div>
  </div>
  <div class="contact" style="left:914px">
    <div class="contact-icon"><svg width="20" height="16" viewBox="0 0 24 18"><rect x="0" y="0" width="24" height="18" rx="2" fill="#111"/><path d="M1 2l11 8 11-8" stroke="#fcc419" stroke-width="2" fill="none"/></svg></div>
    <div><b>email</b><span>info@wefoundtrail.com</span></div>
  </div>
  <div class="copyright">©Copyrights 2024 &nbsp;wefoundtrail &nbsp;&nbsp;| &nbsp;&nbsp;All Rights Reserved</div>
</footer>

</body>
</html>
```